Bookcover: Lessons From the Silent Orchard

I am publishing a super-low-cost innovation book for €4,99 on Bravolo Self Release to help everyone become a great innovator: young ambitious people without college education nor a big budget. Do you want to help me?

Brief:
Design a book cover 1600 x 2560 pixels for BSR.
Main title: Lessons From the Silent Orchard
Sub title: mindset - insights - skills & tools
Author: Maarten de Klerk
Design: captive, and appealing to everyone
Target Group: young ambitious people without college education

For bravolo please format the height/width ratio of 1.6:1

```html
<!DOCTYPE html>
<html lang="en">
<head>
<meta charset="utf-8">
<title>Lessons From the Silent Orchard — Book Cover</title>
<link rel="stylesheet" href="https://fonts.googleapis.com/css2?family=Roboto+Condensed:wght@700;800&display=swap">
<style>
  :root {
    --page-bg: #ffffff;
    --sky: #d7ebf8;
    --band-blue: #4a95d1;
    --navy: #1c2a38;
    --white: #ffffff;
  }
  html, body {
    margin: 0;
    padding: 0;
    width: 1200px;
    height: 1200px;
    overflow: hidden;
    background: var(--page-bg);
  }
  .canvas {
    position: relative;
    width: 1200px;
    height: 1200px;
    background: var(--page-bg);
  }
  .cover {
    position: absolute;
    left: 287px;
    top: 100px;
    width: 625px;
    height: 1000px;
    background: var(--sky);
    overflow: hidden;
  }
  .cover-shapes {
    position: absolute;
    inset: 0;
    width: 100%;
    height: 100%;
  }
  .title {
    position: absolute;
    left: 88px;
    top: 178px;
    margin: 0;
    font-family: "Roboto Condensed", "Arial Narrow", sans-serif;
    font-weight: 800;
    font-size: 110px;
    line-height: 104px;
    letter-spacing: -1px;
    color: var(--white);
    text-transform: uppercase;
    text-shadow: 3px 3px 0 var(--navy), 6px 6px 0 var(--navy), 9px 8px 0 var(--navy);
  }
  .title span { display: block; }
  .subtitle {
    position: absolute;
    left: 0;
    right: 0;
    top: 772px;
    margin: 0;
    text-align: center;
    font-family: "Roboto Condensed", "Arial Narrow", sans-serif;
    font-weight: 700;
    font-size: 26px;
    color: var(--white);
    text-transform: uppercase;
    letter-spacing: 0.5px;
  }
  .author {
    position: absolute;
    left: 0;
    right: 0;
    top: 826px;
    margin: 0;
    text-align: center;
    font-family: "Roboto Condensed", "Arial Narrow", sans-serif;
    font-weight: 700;
    font-size: 38px;
    color: var(--white);
    text-transform: uppercase;
  }
  .idea-icon {
    position: absolute;
    left: 520px;
    top: 40px;
    width: 76px;
    height: 96px;
  }
</style>
</head>
<body>
  <div class="canvas">
    <section class="cover">
      <svg class="cover-shapes" viewBox="0 0 625 1000" preserveAspectRatio="none" aria-hidden="true">
        <polygon fill="var(--band-blue)" points="0,105 70,165 70,760 0,850"/>
        <polygon fill="var(--navy)" points="70,170 300,190 470,430 520,720 625,870 625,1000 0,1000 0,850 70,760"/>
      </svg>

      <h1 class="title">
        <span>Lessons</span>
        <span>From the</span>
        <span>Silent</span>
        <span>Orchard</span>
      </h1>

      <p class="subtitle">Mindset · Insights · Skills &amp; Tools</p>
      <p class="author">Maarten de Klerk</p>

      <svg class="idea-icon" viewBox="0 0 80 100" aria-hidden="true" fill="none" stroke="var(--navy)" stroke-width="3" stroke-linecap="round">
        <line x1="40" y1="4" x2="40" y2="16"/>
        <line x1="14" y1="14" x2="21" y2="22"/>
        <line x1="66" y1="14" x2="59" y2="22"/>
        <line x1="4" y1="40" x2="14" y2="40"/>
        <line x1="76" y1="40" x2="66" y2="40"/>
        <line x1="10" y1="62" x2="18" y2="57"/>
        <line x1="70" y1="62" x2="62" y2="57"/>
        <path d="M40 26 C28 26 21 35 21 45 C21 53 27 58 30 64 L30 72 L50 72 L50 64 C53 58 59 53 59 45 C59 35 52 26 40 26 Z" fill="var(--white)"/>
        <path d="M35 64 L35 50 Q40 44 45 50 L45 64"/>
        <rect x="31" y="74" width="18" height="10" rx="2" fill="var(--navy)"/>
        <line x1="35" y1="88" x2="45" y2="88"/>
      </svg>
    </section>
  </div>
</body>
</html>
```